Core Value Graphic for a Service Disabled and Minority Certified contractor

My company, Bridgewater Service Partners, is a US Federal Contractor that hires veterans and service disabled veterans. Our website is www.bridgewater7.example. We work hard to maintain a 50:50 split between veterans and non-veterans on our team. Our tagline is "To Find a Better Way." We are continually looking to integrate technology and efficiency into all that we do.

I want a way to express our company core values visually so that our employees and customers alike can read them and get a sense of who we are, what drives us to succeed, and what makes up our team DNA.

I need an artist like you to help me represent our core values visually. In a manner that I can print it out on an 8"X11" sheet of paper or a large 48" X 48" poster, without losing the visual clarity or that it pixelates out of focus. I am looking for a color scheme that is patriotic with Red, White, and Blues and similar hues. I would also like to incorporate my logo and tagline into the design in some manner.

I have attached several examples of a Core Value Grids from other companies. I am hopeful it will inspire you, and a get your brain juices flowing to provide me with a knockout Core Value Grid that will rock only you can provide! I also include a copy of my company Core Values and a copy of our Logo.

Looking forward to seeing your creations. Thanks.

Employees, any potential strategic alliance partners, and customers.

Contractor

• Patriotic feel and have my logo someplace on the document.

```html
<!DOCTYPE html>
<html lang="en">
<head>
<meta charset="utf-8">
<title>Core Values – Bridgewater Service Partners</title>
<link href="https://fonts.googleapis.com/css2?family=Montserrat:wght@500;600&family=Oswald:wght@300;400&family=Roboto+Condensed:wght@400;700&display=swap" rel="stylesheet">
<style>
  :root{
    --page-bg:#d1d1d1;
    --sheet:#fbfbfb;
    --red:#ae1018;
    --navy:#13294b;
    --panel:#fffbc6;
    --green:#d4df2b;
    --green-edge:#9fb81c;
    --blue:#29a8df;
    --blue-edge:#1b8cc4;
    --salmon:#f4877f;
    --salmon-edge:#d9534b;
    --orange:#fbb321;
    --orange-edge:#e38f0c;
    --lavender:#b9b0d9;
    --lavender-edge:#8a7fb8;
    --halo:#f4f0b0;
  }
  *{box-sizing:border-box;margin:0;padding:0}
  html,body{width:1200px;height:771px;overflow:hidden}
  body{background:var(--page-bg);position:relative;font-family:"Roboto Condensed",Arial,sans-serif}
  .sheet{position:absolute;left:188px;top:94px;width:822px;height:582px;background:var(--sheet)}
  .tagline-band{position:absolute;left:188px;top:129px;width:822px;height:37px;background:var(--red)}
  .tagline{position:absolute;left:225px;top:135px;color:#fff;font-family:"Montserrat",Arial,sans-serif;font-weight:600;font-size:19.5px;letter-spacing:-.3px}
  .site-url{position:absolute;right:410px;top:142px;color:#fff;font-family:"Montserrat",Arial,sans-serif;font-weight:500;font-size:9px;letter-spacing:.4px;white-space:nowrap}
  .brand-box{position:absolute;left:799px;top:113px;width:163px;height:67px;background:#fff;display:flex;flex-direction:column;justify-content:center;align-items:center}
  .brand-name{font-family:"Montserrat",Arial,sans-serif;font-weight:600;color:var(--navy);font-size:13.5px;line-height:1.1;text-align:center;letter-spacing:.2px}
  .values-frame{position:absolute;left:222px;top:206px;width:756px;height:440px;background:var(--panel);border:2.5px solid var(--navy);border-radius:12px}
  .values-pill{position:absolute;left:510px;top:189px;width:179px;height:33px;background:var(--red);border:2.5px solid var(--navy);border-radius:17px;color:#fff;font-family:"Montserrat",Arial,sans-serif;font-weight:600;font-size:12px;display:flex;align-items:center;justify-content:center}
  .value-card{position:absolute;top:238px;width:132px;height:383px;border-radius:3px;border:1.5px solid;box-shadow:0 0 0 3px var(--halo);text-align:center;padding:0 9px}
  .value-card.green{left:244px;background:var(--green);border-color:var(--green-edge)}
  .value-card.blue{left:389px;background:var(--blue);border-color:var(--blue-edge);color:#fff}
  .value-card.salmon{left:534px;background:var(--salmon);border-color:var(--salmon-edge)}
  .value-card.orange{left:678px;background:var(--orange);border-color:var(--orange-edge)}
  .value-card.lavender{left:824px;background:var(--lavender);border-color:var(--lavender-edge)}
  .value-title{height:56px;display:flex;align-items:center;justify-content:center;font-family:"Oswald",Arial,sans-serif;font-weight:300;font-size:11px;line-height:1.35;color:#1c1c1c;padding-top:2px}
  .blue .value-title{color:#fff}
  .value-icon{display:block;margin:0 auto;width:68px;height:68px}
  .value-body{margin-top:16px;font-size:7.2px;line-height:10px;color:#2a2a2a}
  .blue .value-body{color:#fff}
  .value-body h3{font-size:6.6px;font-weight:700;color:var(--navy);letter-spacing:.2px;margin:2px 0 3px}
  .blue .value-body h3{color:#fff}
  .value-body p{margin-bottom:3px}
</style>
</head>
<body>
  <div class="sheet"></div>
  <div class="tagline-band"></div>
  <div class="tagline">TO FIND A BETTER WAY</div>
  <div class="site-url">www.bridgewater7.example</div>
  <div class="brand-box">
    <div class="brand-name">BRIDGEWATER<br>SERVICE PARTNERS</div>
  </div>

  <div class="values-frame"></div>
  <div class="values-pill">OUR CORE VALUES</div>

  <section class="value-card green">
    <div class="value-title">Everyone comes<br>back to the Green Zone</div>
    <svg class="value-icon" role="img" aria-label="Illustration: tree inside circular green arrows" viewBox="0 0 68 68"><circle cx="34" cy="34" r="32" fill="#3aa843" opacity=".55"/></svg>
    <div class="value-body">
      <h3>WHAT IT MEANS</h3>
      <p>Safety takes precedence over every phase of the day's operation.</p>
      <h3>HOW TO EXPRESS IT</h3>
      <p>Anyone can call a stop to the work in progress if an unsafe act is occurring. In fact, it is each team member's duty to do so, rectify the unsafe issue, then proceed. Never hesitate; everyone comes back. Finally, each After Action Review begins with discussing safety issues. We always let everyone on the team know of an unsafe situation, so it can be avoided in the future.</p>
      <h3>RESULT</h3>
      <p>All team members go home to their loved ones each day to pursue their individual</p>
    </div>
  </section>

  <section class="value-card blue">
    <div class="value-title">Boldly go. Seek. Find.</div>
    <svg class="value-icon" role="img" aria-label="Illustration: red binoculars" viewBox="0 0 68 68"><circle cx="34" cy="34" r="32" fill="#7fcbef"/></svg>
    <div class="value-body">
      <h3>WHAT IT MEANS</h3>
      <p>We weave innovation into the fabric that makes up our company.</p>
      <h3>HOW TO EXPRESS IT</h3>
      <p>We're early adopters of technology. We quickly evaluate new technologies or processes that could separate us from our competition. Then we implement and evaluate these new technologies. We dump it quickly if we see it is not helping us achieve "Commander's Intent." We have the guts to be first. We iterate continuously and attack, attack, attack.</p>
      <h3>RESULT</h3>
      <p>We will be ahead of our competition. It' one mechanism that helps us scale. Prosperity</p>
    </div>
  </section>

  <section class="value-card salmon">
    <div class="value-title">Never leave your<br>wingman</div>
    <svg class="value-icon" role="img" aria-label="Illustration: team member in red cap" viewBox="0 0 68 68"><circle cx="34" cy="34" r="32" fill="#e8453c" opacity=".6"/></svg>
    <div class="value-body">
      <h3>WHAT IT MEANS</h3>
      <p>We always help your team members be successful. Commitment to each other and to our own personal integrity is the fuel that empowers us.</p>
      <h3>HOW TO EXPRESS IT</h3>
      <p>If a Wingman is having challenges accomplishing their individual priorities or completing their assigned mission, volunteer to help them to do so. This goes for Subs/Suppliersas well.We help those who help us succeed! Always look to establish the best win-win relationship possible, and do what you can to support them if they get into a bind.</p>
      <h3>RESULT</h3>
      <p>Be there for them and they will be there for us.</p>
    </div>
  </section>

  <section class="value-card orange">
    <div class="value-title">Fail<br>quickly and learn</div>
    <svg class="value-icon" role="img" aria-label="Illustration: open book" viewBox="0 0 68 68"><circle cx="34" cy="34" r="32" fill="#ffe81a"/></svg>
    <div class="value-body">
      <h3>WHAT IT MEANS</h3>
      <p>If you're not making mistakes, you're not taking enough chances or getting out of your comfort zone.</p>
      <h3>HOW TO EXPRESS IT</h3>
      <p>Use your best judgment when trying something new. But, don't let your pride keep you from saying, "I was wrong" when your idea doesn't work. We trust you will know when it's time to dump the idea, or stop doing something that doesn't work.</p>
      <h3>RESULT</h3>
      <p>No one will ever be penalized for making a mistake. Don't be afraid to try something you believe will work. That's how we grow ourselves and our team members.</p>
    </div>
  </section>

  <section class="value-card lavender">
    <div class="value-title">Troops (Team Members)<br>eat first</div>
    <svg class="value-icon" role="img" aria-label="Illustration: leader with team members" viewBox="0 0 68 68"><circle cx="34" cy="34" r="32" fill="#7468a8" opacity=".45"/></svg>
    <div class="value-body">
      <h3>WHAT IT MEANS</h3>
      <p>No leader will put themselves ahead of their subordinates.</p>
      <h3>HOW TO EXPRESS IT</h3>
      <p>We lead by example. Demonstrate the moral courage and discipline to do the right thing at the highest level of quality.</p>
      <h3>RESULT</h3>
      <p>Every new team member's will quickly realize their leaders genuinely care for their welfare and success This is the best way to drive Esprit de Corps and achieve excellence.</p>
    </div>
  </section>
</body>
</html>
```